Fun family flyer for photographer

Need a flyer to promote our business moving to Brisbane.

Require a family friendly look targetted to mothers, using our logo and existing images from previous shoots.

Would like to see designs that feature the images heavily, but still have text and fonts that set it aside from other flyers.
Updates

I would like to see some unique fonts being used, so far I have only recieved "canned" fonts, some were just straight out Adobe fonts (on a design site? Really?).

Some SUGGESTIONS would include font use similar to the following:
http://www.glyphyard.net/oldpress.font
http://www.glyphyard.net/happy-otter.font

Fun fonts, something that grabs attention.
If you're going to plonk one image in the middle of the page and fill it with text in Courier New, consider not submitting.

I would like colourful, attention grabbing backgrounds.

Target Market(s)

Families

Industry/Entity Type

Business

Requirements
Must have
• Two sides to the flyer
Focus on "fun"
Targetted to mothers
Nice to have
• All photos attached, not necessary but nice.
Should not have
• Anything too "corporate"

```html
<!DOCTYPE html>
<html lang="en">
<head>
<meta charset="utf-8">
<title>Blue Kite Frames – Contact</title>
<link rel="stylesheet" href="https://fonts.googleapis.com/css2?family=Arimo:wght@400;700&display=swap">
<style>
  :root {
    --paper: #ffffff;
    --ink-blue: #2a7ab0;
    --star-blue: #2f7fb8;
    --frame-blue: #a9cde8;
    --frame-edge: #7fb3dc;
    --lime: #c8d400;
    --photo-top: #8a8580;
    --photo-mid: #6e6660;
    --photo-low: #9fb4cf;
    --swirl-a: #e6e23a;
    --swirl-b: #2bb3c0;
    --swirl-c: #3f5fb0;
    --swirl-d: #8a3d9a;
    --swirl-e: #2f9a5a;
  }
  * { margin: 0; padding: 0; box-sizing: border-box; }
  html, body { width: 773px; height: 1200px; overflow: hidden; background: var(--paper); }
  .flyer-back {
    position: relative;
    width: 773px;
    height: 1200px;
    background: var(--paper);
    font-family: "Arimo", Arial, sans-serif;
    overflow: hidden;
  }
  .hanging-stars {
    position: absolute;
    left: 4px; top: 0;
    width: 138px; height: 292px;
    background: linear-gradient(180deg, rgba(47,127,184,0.55), rgba(47,127,184,0.25));
    border-radius: 0 0 40px 40px;
  }
  .swirl-art {
    position: absolute;
    left: 511px; top: 52px;
    width: 262px; height: 1148px;
    border-radius: 130px 0 0 130px;
    background: linear-gradient(180deg,
      var(--swirl-a) 0%, var(--swirl-b) 30%, var(--swirl-c) 48%,
      var(--swirl-d) 62%, var(--swirl-e) 85%, var(--swirl-b) 100%);
    opacity: 0.9;
  }
  .photo-frame {
    position: absolute;
    left: 142px; top: 182px;
    width: 355px; height: 411px;
    background: var(--frame-blue);
    border: 2px solid var(--frame-edge);
    box-shadow: 0 2px 4px rgba(0,0,0,0.25);
  }
  .photo-frame .photo {
    position: absolute;
    left: 21px; top: 15px;
    width: 313px; height: 370px;
    background: linear-gradient(180deg, var(--photo-top) 0%, var(--photo-mid) 55%, var(--photo-low) 100%);
  }
  .ground-band {
    position: absolute;
    left: 0; top: 0;
    width: 773px; height: 1200px;
  }
  .contact {
    position: absolute;
    left: 0; top: 0;
    width: 773px;
    color: var(--ink-blue);
  }
  .contact-heading {
    position: absolute;
    left: 0; width: 538px; top: 718px;
    text-align: center;
    font-size: 43px;
    font-weight: 400;
    letter-spacing: 0.2px;
  }
  .contact-line {
    position: absolute;
    font-size: 38px;
    white-space: nowrap;
  }
  .contact-web { left: 34px; top: 796px; font-size: 37px; }
  .contact-phone { left: 76px; top: 866px; }
  .contact-phone .gap { display: inline-block; width: 32px; }
  .contact-mail { left: 33px; top: 937px; font-size: 37px; }
  .brand-mark {
    position: absolute;
    left: 6px; top: 1126px;
    display: flex;
    align-items: center;
    gap: 6px;
    color: var(--ink-blue);
    font-size: 18px;
    font-weight: 700;
  }
  .brand-mark .brand-square {
    width: 14px; height: 14px;
    background: var(--ink-blue);
  }
</style>
</head>
<body>
  <main class="flyer-back">
    <div class="hanging-stars" role="img" aria-label="Hanging blue star decorations"></div>
    <div class="swirl-art" role="img" aria-label="Colourful swirling illustration with flowers and stars"></div>

    <svg class="ground-band" viewBox="0 0 773 1200" aria-hidden="true">
      <polygon points="0,1168 773,1091 773,1200 0,1200" fill="var(--lime)"/>
    </svg>

    <figure class="photo-frame">
      <div class="photo" role="img" aria-label="Photo of a baby sitting in front of a large turtle sculpture"></div>
    </figure>

    <section class="contact">
      <h2 class="contact-heading">Contact details</h2>
      <p class="contact-line contact-web">/http://bluekiteframes.com.au</p>
      <p class="contact-line contact-phone">phone :<span class="gap"></span>0491570156</p>
      <p class="contact-line contact-mail">info@bluekiteframes.com.au</p>
    </section>

    <div class="brand-mark">
      <span class="brand-square"></span>
      <span class="brand-name">Blue Kite</span>
    </div>
  </main>
</body>
</html>
```